Web design for small empirical brand consulting company that will sell a web-based brand tool

We need a totally new and very appealing website:
Purpose: We want to attract lots of potential customers with this website... especially, we want to sell our web-based tool markvista®... we want to be perceived as innovative, trendy, but solid and reliable… we want customers go to the website, login at „markvista®“ (see structure), and perceive how it works.. and the contacting us or in the near future being able to buy a login and work with the tool… so we want to a) inform (on the website or send the url to customers) and b) to „force“ potential customers getting in contact with us…
Structure (e.g.): Must Home, markvista®, About us, Contact (incl. legal notice); we are open for more, Nice to have e.g. references/clients, press... for example, we publish a nice book in a couple of months and might want to show it somewhere on the website as well...)
Layout: We would like to have more/mainly figures - may be animated or something like that – in specific those on slides 7 and 8 as well as 6 and 9 (which would be for our web-based tool markvista®...)... excellent, but simple and with few text…
Fonts: Eurostile; CMYK 100/23/100/19, CMYK 0/0/0/70
Logo: Would you please use the trelloway-logo used in this file?
Social Media: we think that it might make sense to be connected to facebook, twitter and so on as well…
Phantasy: May be it is possible to have something between a classic marketing research and an e-commerce website... just a thought... because it is mainly about the new tool that will be assessable through a login... but customers might want to contact us or vice versa in order to check how the tool will work (btw: you do not have further info about markvista® here... I know)… I dream of having a site where people go to and by components of our tool like at zorvik… click and buy and go for it…
It is possible to program it in php or java? Thanks.
Pages I personally like: Don’t know if that helps, but I personally like those websites just they seem so simple: http:// www.pelvarion.com/, http://www.quintabel.net/... but I am veeery open
Pages I do not like anymore: my own www.trelloway.ch

```html
<!DOCTYPE html>
<html lang="en">
<head>
<meta charset="utf-8">
<title>trelloway – Brand measurement and modelling</title>
<link href="https://fonts.googleapis.com/css2?family=Mulish:wght@300;400;600;700;800&display=swap" rel="stylesheet">
<style>
:root{
  --green:#137c3e;
  --green-dark:#0f6c35;
  --green-box:#1f8f4c;
  --grey-text:#555;
  --grey-dark:#4a4a4a;
  --grey-darker:#383838;
  --light:#f2f2f2;
  --white:#fff;
}
*{box-sizing:border-box;margin:0;padding:0}
html,body{width:1200px;height:2871px;overflow:hidden}
body{font-family:"Mulish",Arial,sans-serif;color:var(--grey-text);background:var(--white);position:relative}
a{color:inherit;text-decoration:none}

/* header */
.site-header{position:absolute;top:0;left:0;width:1200px;height:92px;background:#fff;box-shadow:0 2px 6px rgba(0,0,0,.12);z-index:2}
.logo{position:absolute;left:73px;top:26px;display:flex;align-items:center;gap:8px;font-size:36px;font-weight:600;color:var(--green);letter-spacing:-.5px;line-height:40px}
.logo-mark{width:12px;height:34px;background:var(--green)}
.main-nav{position:absolute;right:73px;top:0;height:92px;display:flex;align-items:center;gap:52px;font-size:15px;color:#666}
.main-nav .current{color:#222;font-weight:600}
.login-btn{background:var(--green);color:#fff;font-size:13px;font-weight:600;padding:9px 22px;border-radius:2px;margin-left:-10px}

/* hero */
.hero{position:absolute;top:92px;left:0;width:1200px;height:448px;background:linear-gradient(90deg,#c9d0d2 0%,#e4e8e7 35%,#f1efeb 60%,#d9c8b5 80%,#b9a58f 100%)}
.hero-caption{position:absolute;left:75px;top:130px;width:616px;height:186px;background:rgba(255,255,255,.85);border:1px solid #ddd;padding:22px 18px}
.hero-caption h1{font-size:30px;font-weight:400;color:#222;line-height:38px;text-transform:uppercase}
.hero-caption p{margin-top:10px;font-size:15px;font-weight:700;color:var(--green);line-height:20px}
.hero-dots{position:absolute;left:75px;top:415px;display:flex;gap:6px}
.hero-dots span{width:10px;height:10px;border-radius:50%;background:#333}

/* section titles */
.section-title{position:absolute;left:0;width:1200px;text-align:center;font-size:29px;font-weight:400;text-transform:uppercase;color:var(--green)}
.on-green .section-title{color:#fff}

/* welcome */
.welcome{position:absolute;top:540px;left:0;width:1200px;height:528px}
.welcome .section-title{top:36px}
.feature{position:absolute;top:105px;width:320px;text-align:center}
.feature-photo{width:180px;height:180px;border-radius:50%;margin:0 auto}
.feature h3{margin-top:34px;font-size:19px;font-weight:400;color:#222;text-transform:uppercase}
.feature p{margin-top:8px;font-size:12.5px;line-height:20px}
.feature .more{display:block;margin-top:16px;font-size:12px;color:var(--green);font-weight:600}

/* benefits */
.benefits{position:absolute;top:1068px;left:0;width:1200px;height:740px;background:var(--green)}
.benefits .section-title{top:36px}
.benefits .lead{position:absolute;top:92px;width:1200px;text-align:center;color:#fff;font-size:14px}
.benefit{position:absolute;width:245px;height:264px}
.benefit-icon{position:absolute;left:67px;top:0;width:111px;height:111px;border-radius:50%;background:#fff;display:flex;align-items:center;justify-content:center;z-index:1}
.benefit-box{position:absolute;top:128px;left:0;width:245px;height:136px;background:var(--green-box);color:#fff;text-align:center;padding:18px 16px 0}
.benefit-box::before{content:"";position:absolute;top:-10px;left:112px;border-left:11px solid transparent;border-right:11px solid transparent;border-bottom:10px solid var(--green-box)}
.benefit-box h4{font-size:18px;font-weight:400;line-height:20px}
.benefit-box p{margin-top:9px;font-size:12px;line-height:19px}

/* work */
.work{position:absolute;top:1808px;left:0;width:1200px;height:382px}
.work-visual{position:absolute;left:73px;top:97px;width:434px;height:235px;background:linear-gradient(180deg,#e8ebea 0%,#cdd3d1 85%,#b0b4b3 100%);border-radius:8px}
.work h2{position:absolute;left:568px;top:42px;font-size:29px;font-weight:400;color:var(--green)}
.work-text{position:absolute;left:568px;top:90px;width:605px;font-size:12.5px;line-height:19.5px}
.work-text p+p{margin-top:8px}
.btn{position:absolute;left:570px;top:293px;width:134px;height:37px;background:var(--green);color:#fff;font-size:12px;font-weight:600;display:flex;align-items:center;justify-content:center}

/* about */
.about{position:absolute;top:2190px;left:0;width:1200px;height:288px;background:var(--green)}
.about .section-title{top:34px}
.about .lead{position:absolute;left:75px;top:88px;width:1050px;text-align:center;color:#fff;font-size:12.5px;line-height:20px}
.member{position:absolute;top:149px;width:245px;height:92px;background:var(--light);padding:14px 12px;display:flex;gap:20px}
.member-photo{width:52px;height:62px;background:linear-gradient(180deg,#d8c7b4,#a98f76);flex:none}
.member h5{font-size:13px;font-weight:600;color:var(--green)}
.member p{font-size:12px;margin-top:4px}
.member .social{display:flex;gap:5px;margin-top:8px}
.member .social span{width:20px;height:20px;border-radius:50%;background:#9a9a9a}

/* clients */
.clients{position:absolute;top:2478px;left:0;width:1200px;height:162px}
.clients .section-title{top:26px}
.client-row{position:absolute;top:88px;left:160px;width:880px;display:flex;justify-content:space-between;align-items:center;font-size:20px;font-weight:700;color:var(--grey-dark)}

/* footer */
.site-footer{position:absolute;top:2640px;left:0;width:1200px;height:178px;background:var(--grey-dark);color:#ddd}
.footer-col{position:absolute;top:32px}
.footer-col h6{font-size:15px;font-weight:400;color:#fff;margin-bottom:14px}
.footer-col p{font-size:12px;line-height:19px;color:#ccc}
.footer-col .muted{color:var(--green-box);margin-top:4px}
.footer-col .read{display:block;margin-top:14px;font-size:11px;color:#fff;font-weight:700}
.newsletter{display:flex;height:30px}
.newsletter span{width:196px;background:#eee;color:#888;font-size:12px;font-style:italic;padding:7px 12px}
.newsletter b{width:34px;background:var(--green);display:flex;align-items:center;justify-content:center}
.footer-col .mail{color:var(--green-box)}
.connect{display:flex;gap:6px}
.connect span{width:28px;height:28px;border-radius:50%;background:#f2f2f2}
.copyright{position:absolute;top:2818px;left:0;width:1200px;height:53px;background:var(--grey-darker);color:#aaa;font-size:11px;text-align:center;line-height:53px}
</style>
</head>
<body>

<header class="site-header">
  <div class="logo"><span class="logo-mark"></span>trelloway</div>
  <nav class="main-nav">
    <a class="current">Home</a><a>Services</a><a>Work</a><a>Credentials</a><a>Contact</a>
    <a class="login-btn">LOG IN</a>
  </nav>
</header>

<section class="hero" role="img" aria-label="Photo of a smiling businesswoman in a bright office, colleagues blurred behind her">
  <div class="hero-caption">
    <h1>We measure, test and model your<br>brand and your success&nbsp;»</h1>
    <p>Duis aliquam nibh a dui iaculis viverra id a velit. Vivamus egestas risus in magna varius commodo. Sed semper viverra egestas. Etiam pretium porttitor lectus, vel ornare neque porta volutpat.</p>
  </div>
  <div class="hero-dots"><span></span><span></span><span></span><span></span></div>
</section>

<section class="welcome">
  <h2 class="section-title">Welcome to our website</h2>
  <div class="feature" style="left:79px">
    <div class="feature-photo" role="img" aria-label="Illustration of branding gears and business handshake" style="background:radial-gradient(circle,#7a4f8c,#2f3c5a 70%,#1b2233)"></div>
    <h3>Company Brand</h3>
    <p>Aliquam molestie, mi et imperdiet euismod, dui purus auctor tellus, et interdum lacus lectus et ante. Sed accumsan sollicitudin sapien, sit amet adipiscing turpis gravida ac.</p>
    <a class="more">LEARN MORE ››</a>
  </div>
  <div class="feature" style="left:439px">
    <div class="feature-photo" role="img" aria-label="Photo of customer service staff with headsets" style="background:radial-gradient(circle,#e8d7c6,#b79779 75%,#8a6e58)"></div>
    <h3>Product / Services</h3>
    <p>Aliquam molestie, mi et imperdiet euismod, dui purus auctor tellus, et interdum lacus lectus et ante. Sed accumsan sollicitudin sapien, sit amet adipiscing turpis gravida ac.</p>
    <a class="more">LEARN MORE ››</a>
  </div>
  <div class="feature" style="left:799px">
    <div class="feature-photo" role="img" aria-label="Photo of a presenter at a whiteboard in a meeting" style="background:radial-gradient(circle,#f4f6f8,#cfd8e0 70%,#9fb0c0)"></div>
    <h3>CEO Brand</h3>
    <p>Aliquam molestie, mi et imperdiet euismod, dui purus auctor tellus, et interdum lacus lectus et ante. Sed accumsan sollicitudin sapien, sit amet adipiscing turpis gravida ac.</p>
    <a class="more">LEARN MORE ››</a>
  </div>
</section>

<section class="benefits on-green">
  <h2 class="section-title">Our benefits</h2>
  <p class="lead">More successful market development and activities through sound brand analysis and trend modeling using markvista®»</p>

  <div class="benefit" style="left:73px;top:138px">
    <div class="benefit-icon"><svg width="56" height="56" viewBox="0 0 56 56"><circle cx="28" cy="28" r="22" fill="none" stroke="#137c3e" stroke-width="5"/><path d="M28 12 A16 16 0 1 0 44 28 L28 28Z" fill="#137c3e"/><path d="M31 10 A16 16 0 0 1 46 25 L31 25Z" fill="#137c3e"/></svg></div>
    <div class="benefit-box"><h4>Metrics</h4><p>Duis aliquam nibh a dui iaculis viverra id a velit. Vivamus egestas risus in magna varius commodo.</p></div>
  </div>
  <div class="benefit" style="left:343px;top:138px">
    <div class="benefit-icon"><svg width="58" height="56" viewBox="0 0 58 56"><rect x="6" y="38" width="8" height="14" fill="#137c3e"/><rect x="18" y="30" width="8" height="22" fill="#137c3e"/><rect x="30" y="22" width="8" height="30" fill="#137c3e"/><rect x="42" y="14" width="8" height="38" fill="#137c3e"/><path d="M4 30 L22 16 L32 22 L48 6" fill="none" stroke="#137c3e" stroke-width="4"/><path d="M40 4 L52 3 L50 15Z" fill="#137c3e"/></svg></div>
    <div class="benefit-box"><h4>Trend Models</h4><p>Duis aliquam nibh a dui iaculis viverra id a velit. Vivamus egestas risus in magna varius commodo.</p></div>
  </div>
  <div class="benefit" style="left:613px;top:138px">
    <div class="benefit-icon"><svg width="54" height="54" viewBox="0 0 54 54"><path d="M10 44 L42 12" stroke="#137c3e" stroke-width="8" stroke-linecap="round"/><path d="M12 12 L44 44" stroke="#137c3e" stroke-width="6" stroke-linecap="round"/><circle cx="44" cy="10" r="7" fill="none" stroke="#137c3e" stroke-width="4"/></svg></div>
    <div class="benefit-box"><h4>Precision</h4><p>Duis aliquam nibh a dui iaculis viverra id a velit. Vivamus egestas risus in magna varius commodo.</p></div>
  </div>
  <div class="benefit" style="left:883px;top:138px">
    <div class="benefit-icon"><svg width="56" height="56" viewBox="0 0 56 56"><circle cx="28" cy="28" r="22" fill="none" stroke="#137c3e" stroke-width="5"/><text x="28" y="38" text-anchor="middle" font-family="Mulish,sans-serif" font-weight="800" font-size="28" fill="#137c3e">$</text></svg></div>
    <div class="benefit-box"><h4>Cost Reduction</h4><p>Duis aliquam nibh a dui iaculis viverra id a velit. Vivamus egestas risus in magna varius commodo.</p></div>
  </div>

  <div class="benefit" style="left:73px;top:425px">
    <div class="benefit-icon"><svg width="60" height="44" viewBox="0 0 60 44"><path d="M2 14 L16 6 L30 14 L44 6 L58 14 L50 30 L36 40 L22 36 L10 28Z" fill="#137c3e"/></svg></div>
    <div class="benefit-box"><h4>Closeness</h4><p>Duis aliquam nibh a dui iaculis viverra id a velit. Vivamus egestas risus in magna varius commodo.</p></div>
  </div>
  <div class="benefit" style="left:343px;top:425px">
    <div class="benefit-icon"><svg width="56" height="56" viewBox="0 0 56 56"><g stroke="#137c3e" stroke-width="4" fill="none"><circle cx="12" cy="12" r="7"/><circle cx="44" cy="12" r="7"/><circle cx="12" cy="44" r="7"/><path d="M19 12 H37 M12 19 V37"/></g><rect x="34" y="36" width="18" height="14" fill="#137c3e"/><path d="M37 36 V31 A6 6 0 0 1 49 31 V36" stroke="#137c3e" stroke-width="3" fill="none"/></svg></div>
    <div class="benefit-box"><h4>Security</h4><p>Duis aliquam nibh a dui iaculis viverra id a velit. Vivamus egestas risus in magna varius commodo.</p></div>
  </div>
  <div class="benefit" style="left:613px;top:425px">
    <div class="benefit-icon"><svg width="58" height="44" viewBox="0 0 58 44"><rect x="23" y="4" width="4" height="36" fill="#137c3e"/><rect x="31" y="4" width="4" height="36" fill="#137c3e"/><path d="M19 22 L4 10 V34Z M39 22 L54 10 V34Z" fill="#137c3e"/></svg></div>
    <div class="benefit-box"><h4>Fit</h4><p>Duis aliquam nibh a dui iaculis viverra id a velit. Vivamus egestas risus in magna varius commodo.</p></div>
  </div>
  <div class="benefit" style="left:883px;top:425px">
    <div class="benefit-icon"><svg width="62" height="44" viewBox="0 0 62 44"><g fill="#137c3e"><circle cx="14" cy="12" r="6"/><circle cx="31" cy="9" r="7"/><circle cx="48" cy="12" r="6"/><rect x="4" y="20" width="20" height="16" rx="5"/><rect x="20" y="18" width="22" height="20" rx="6"/><rect x="38" y="20" width="20" height="16" rx="5"/><rect x="2" y="38" width="58" height="4"/></g></svg></div>
    <div class="benefit-box" style="padding-top:12px"><h4>Customer Loyalty/<br>Acquisition</h4><p style="margin-top:6px">Duis aliquam nibh a dui iaculis viverra id a velit. Vivamus egestas risus in magna varius commodo.</p></div>
  </div>
</section>

<section class="work">
  <div class="work-visual" role="img" aria-label="Laptop showing the markvista dashboard with green bar charts"></div>
  <h2>OUR WORK</h2>
  <div class="work-text">
    <p>Aliquam molestie, mi et imperdiet euismod, dui purus auctor tellus, et interdum lacus lectus et ante. Sed accumsan sollicitudin sapien, sit amet adipiscing turpis gravida ac. In congue, neque ac lobortis volutpat, libera mauris varius mi, vitae suscipit ipsum ligula vitae risus. Duis aliquam nibh a dui iaculis viverra id a velit. Vivamus egestas risus in magna varius commodo. Sed semper viverra egestas. Etiam pretium porttitor lectus, vel ornare neque porta volutpat.</p>
    <p>Vestibulum ante ipsum primis in faucibus orci luctus et ultrices posuere cubilia Curae; Ut et scelerisque ante. Donec erat purus, faucibus vitae congue vel, porttitor nec lectus. Aenean a nibh eget turpis vehicula tempus ac sed massa.</p>
  </div>
  <a class="btn">READ MORE ››</a>
</section>

<section class="about on-green">
  <h2 class="section-title">About us</h2>
  <p class="lead">Vestibulum ante ipsum primis in faucibus orci luctus et ultrices posuere cubilia Curae; Ut et scelerisque ante. Donec erat purus, faucibus vitae congue vel, porttitor nec lectus. Aenean a nibh eget turpis vehicula tempus ac sed massa. Vestibulum dolor nulla, ultrices ac tincidunt sed, laoreet non est.</p>
  <div class="member" style="left:73px"><div class="member-photo" role="img" aria-label="Team member portrait"></div><div><h5>Lukas Brenner, Dr.</h5><p>Sed accumsan sollicitudin</p><div class="social"><span></span><span></span><span></span><span></span></div></div></div>
  <div class="member" style="left:343px"><div class="member-photo" role="img" aria-label="Team member portrait"></div><div><h5>Lukas Brenner, Dr.</h5><p>Sed accumsan sollicitudin</p><div class="social"><span></span><span></span><span></span><span></span></div></div></div>
  <div class="member" style="left:613px"><div class="member-photo" role="img" aria-label="Team member portrait"></div><div><h5>Lukas Brenner, Dr.</h5><p>Sed accumsan sollicitudin</p><div class="social"><span></span><span></span><span></span><span></span></div></div></div>
  <div class="member" style="left:883px"><div class="member-photo" role="img" aria-label="Team member sketch portrait" style="background:linear-gradient(180deg,#f1efea,#d6d2ca)"></div><div><h5>Lukas Brenner, Dr.</h5><p>Sed accumsan sollicitudin</p><div class="social"><span></span><span></span><span></span><span></span></div></div></div>
</section>

<section class="clients">
  <h2 class="section-title">Our clients</h2>
  <div class="client-row">
    <span>Fernmoor</span><span>Quillo</span><span>Netwise</span><span>Tarvo</span><span>Olvexa</span><span>Brevon</span><span>Dunmark</span><span>Aldra</span><span>Cyrel</span>
  </div>
</section>

<footer class="site-footer">
  <div class="footer-col" style="left:73px;width:290px">
    <h6>Latest Tweets</h6>
    <p>Aliquam molestie, mi et imperdiet euismod, dui purus auctor tellus, et interdum...</p>
    <p class="muted">2 days ago</p>
    <a class="read">READ ALL ››</a>
  </div>
  <div class="footer-col" style="left:419px">
    <h6>Newsletter Subscribe</h6>
    <div class="newsletter"><span>Enter Email Address</span><b><svg width="14" height="14" viewBox="0 0 14 14"><path d="M3 1 L10 7 L3 13" stroke="#fff" stroke-width="3" fill="none"/></svg></b></div>
  </div>
  <div class="footer-col" style="left:704px">
    <h6>Contact Info</h6>
    <p><b style="color:#eee">Trelloway GmbH</b><br>Lindenweg 14<br>CH-8400 Talberg ZH<br>Tel.: +41 44 000 12 34<br>E-mail: <span class="mail">info@trelloway.ch</span></p>
  </div>
  <div class="footer-col" style="left:945px">
    <h6>Connect Us</h6>
    <div class="connect"><span></span><span></span><span></span><span></span><span></span></div>
  </div>
</footer>
<div class="copyright">Copyright © 2014 Trelloway. All Right Reserved</div>

</body>
</html>
```